brivox new business card design project

we need a new business card design. you can view info about us @ brivox.com. i have attached an example of our previous card with our previous name that we no longer use. We really liked the design, colors etc. look below to see more info about this project. it asks for a limited number of words. please see our website for more info about our compnay.

Target Market(s)

law enforcement

Contact Information for Business Card

i have uploaded an example of what we used before that we liked.

Font styles to use
Serif

```html
<!DOCTYPE html>
<html lang="en">
<head>
<meta charset="utf-8">
<title>Brivox Business Card</title>
<link rel="stylesheet" href="https://fonts.googleapis.com/css2?family=Open+Sans:wght@300;400;600;700&display=swap">
<style>
  :root {
    --page-bg: #e9ebee;
    --navy: #123a52;
    --navy-light: #24607f;
    --ink: #1c1c1c;
    --muted: #9a9a9a;
    --band-grey: #c9cacc;
    --white: #ffffff;
    --rule: #bdbdbd;
  }
  * { box-sizing: border-box; margin: 0; padding: 0; }
  html, body {
    width: 1200px; height: 900px; overflow: hidden;
    background: var(--page-bg);
    font-family: "Open Sans", sans-serif;
  }
  .sheet {
    width: 1200px; height: 900px;
    display: flex; flex-direction: column;
    align-items: center; justify-content: center; gap: 60px;
  }
  .card {
    width: 600px; height: 343px;
    border-radius: 22px; overflow: hidden;
    position: relative;
    box-shadow: 0 10px 30px rgba(0,0,0,0.18);
  }

  /* Front */
  .card-front { background: var(--white); }
  .front-band {
    position: absolute; left: 0; right: 0; bottom: 0; height: 58px;
    background: var(--navy);
    display: flex; align-items: center; justify-content: center;
  }
  .front-address {
    color: var(--white); font-weight: 700; font-size: 20px; letter-spacing: 0.3px;
  }
  .front-body {
    position: absolute; left: 0; right: 0; top: 0; bottom: 58px;
    display: flex; align-items: center;
  }
  .wordmark {
    font-weight: 300; color: var(--ink);
    letter-spacing: 4px; line-height: 1;
  }
  .front-logo { width: 300px; text-align: center; font-size: 52px; }
  .divider {
    width: 1px; height: 160px; background: var(--rule);
  }
  .contact { padding-left: 30px; }
  .contact-name { color: var(--navy); font-weight: 700; font-size: 22px; line-height: 1.1; }
  .contact-title { color: var(--muted); font-size: 14px; margin-top: 2px; }
  .contact-rule { width: 120px; height: 1px; background: var(--rule); margin: 10px 0 10px; }
  .contact-list { list-style: none; }
  .contact-list li {
    display: flex; align-items: center; gap: 8px;
    color: #555; font-size: 14px; line-height: 24px;
  }
  .contact-icon { width: 15px; height: 15px; flex: none; }

  /* Back */
  .card-back {
    background: linear-gradient(160deg, var(--navy) 0%, var(--navy-light) 100%);
  }
  .back-logo {
    position: absolute; left: 0; right: 0; top: 0; bottom: 52px;
    display: flex; align-items: center; justify-content: center;
  }
  .back-logo .wordmark { color: var(--white); font-size: 64px; }
  .back-band {
    position: absolute; left: 0; right: 0; bottom: 0; height: 52px;
    background: linear-gradient(180deg, #d9dadc, var(--band-grey));
    display: flex; align-items: center; justify-content: center;
  }
  .back-url { color: var(--navy); font-weight: 700; font-size: 20px; }
</style>
</head>
<body>
<main class="sheet">
  <section class="card card-front" aria-label="Business card front">
    <div class="front-body">
      <div class="front-logo"><span class="wordmark">BRIVOX</span></div>
      <div class="divider"></div>
      <div class="contact">
        <p class="contact-name">Daniel Marsh</p>
        <p class="contact-title">Founder/Chief Executive Officer</p>
        <div class="contact-rule"></div>
        <ul class="contact-list">
          <li>
            <svg class="contact-icon" viewBox="0 0 16 16" aria-hidden="true">
              <circle cx="8" cy="8" r="8" fill="#123a52"/>
              <path d="M5.2 4.2l1.4 0 .6 1.8-.9.7c.5 1 1.2 1.7 2.2 2.2l.7-.9 1.8.6 0 1.4c-3.3.3-6.1-2.5-5.8-5.8z" fill="#fff"/>
            </svg>555.010.4420
          </li>
          <li>
            <svg class="contact-icon" viewBox="0 0 16 16" aria-hidden="true">
              <circle cx="8" cy="8" r="8" fill="#123a52"/>
              <rect x="4" y="5" width="8" height="6" fill="none" stroke="#fff" stroke-width="1"/>
              <path d="M4 5l4 3 4-3" fill="none" stroke="#fff" stroke-width="1"/>
            </svg>info@brivox.com
          </li>
          <li>
            <svg class="contact-icon" viewBox="0 0 16 16" aria-hidden="true">
              <circle cx="8" cy="8" r="8" fill="#123a52"/>
              <circle cx="8" cy="8" r="4" fill="none" stroke="#fff" stroke-width="1"/>
              <path d="M4 8h8M8 4c-1.6 2-1.6 6 0 8M8 4c1.6 2 1.6 6 0 8" fill="none" stroke="#fff" stroke-width="0.8"/>
            </svg>www.brivox.com
          </li>
        </ul>
      </div>
    </div>
    <div class="front-band"><span class="front-address">2140 Alder Lane, Austin, TX 78701</span></div>
  </section>

  <section class="card card-back" aria-label="Business card back">
    <div class="back-logo"><span class="wordmark">BRIVOX</span></div>
    <div class="back-band"><span class="back-url">www.brivox.com</span></div>
  </section>
</main>
</body>
</html>
```